Business IT Services Billboard to attract local small businesses

We are Brivolane, a premier Managed Service Provider (MSP) specializing in comprehensive IT services and VOIP phone solutions exclusively for businesses. Our goal is to create a dynamic and visually engaging billboard advertisement that not only highlights our cutting-edge IT solutions but also emphasizes our state-of-the-art VOIP phone services. This billboard should communicate our commitment to providing innovative, reliable, and holistic technology solutions.
Target Market(s)
small business
Industry/Entity Type
Information Technology
Colors
Designer to choose colors to be used in the design.
Look and feel
Each slider illustrates characteristics of the customer's brand and the style your logo design should communicate.

```html
<!DOCTYPE html>
<html lang="en">
<head>
<meta charset="utf-8">
<title>Brivolane – IT and VOIP Billboard</title>
<link rel="stylesheet" href="https://fonts.googleapis.com/css2?family=Saira:ital,wght@0,400;0,600;0,700;0,800;1,400;1,700&display=swap">
<style>
  :root {
    --brand-blue: #1577bd;
    --white: #ffffff;
    --stage: #000000;
    --photo-light: #e6f0f8;
    --photo-mid: #8fb4dc;
    --photo-deep: #2f5f9c;
    --photo-warm: #c9a27e;
  }
  html, body {
    margin: 0;
    padding: 0;
    width: 993px;
    height: 1200px;
    overflow: hidden;
    background: var(--stage);
  }
  .billboard {
    position: absolute;
    left: 26px;
    top: 365px;
    width: 940px;
    height: 470px;
    display: block;
    font-family: "Saira", sans-serif;
  }
  .fill-blue { fill: var(--brand-blue); }
  .fill-white { fill: var(--white); }
  .rule { stroke: var(--white); stroke-width: 1; }
  .kicker { font-weight: 700; font-size: 29px; fill: var(--brand-blue); }
  .headline { font-weight: 700; font-size: 66px; fill: var(--white); }
  .connector { font-weight: 700; font-size: 44px; fill: var(--white); }
  .voip { font-weight: 800; font-size: 150px; fill: var(--white); letter-spacing: -2px; }
  .services { font-weight: 600; font-size: 31px; fill: var(--white); }
  .tagline { font-style: italic; font-weight: 400; font-size: 22px; fill: var(--brand-blue); }
  .tagline-strong { font-weight: 700; }
  .cta { font-weight: 600; font-size: 18px; fill: var(--brand-blue); }
  .url { font-weight: 400; font-size: 34px; fill: var(--white); }
  .url-strong { font-weight: 700; }
  .brand-name { font-weight: 800; font-size: 40px; fill: var(--brand-blue); }
</style>
</head>
<body>
<svg class="billboard" viewBox="0 0 940 470" xmlns="http://www.w3.org/2000/svg">
  <defs>
    <linearGradient id="photo-tone" x1="0" y1="0" x2="1" y2="1">
      <stop offset="0" stop-color="var(--photo-light)"/>
      <stop offset="0.45" stop-color="var(--photo-mid)"/>
      <stop offset="0.8" stop-color="var(--photo-deep)"/>
      <stop offset="1" stop-color="var(--photo-warm)"/>
    </linearGradient>
  </defs>

  <!-- photo area -->
  <rect class="photo" x="470" y="0" width="470" height="370" fill="url(#photo-tone)"
        role="img" aria-label="Photo of an office desk phone with a headset resting on it"/>

  <!-- left blue panel -->
  <polygon class="fill-blue" points="0,0 470,0 522,390 0,390"/>
  <!-- bottom left white band -->
  <polygon class="fill-white" points="0,390 522,390 533,470 0,470"/>
  <!-- call-to-action strip -->
  <polygon class="fill-white" points="519,368 940,368 940,390 522,390"/>
  <!-- bottom right blue band -->
  <polygon class="fill-blue" points="522,390 940,390 940,470 533,470"/>

  <!-- brand name -->
  <text class="brand-name" x="743" y="62" text-anchor="middle">Brivolane</text>

  <!-- kicker -->
  <rect class="fill-white" x="29" y="48" width="374" height="40"/>
  <text class="kicker" x="36" y="79">Boost Your Business with</text>

  <!-- headline -->
  <text class="headline" x="28" y="172">Next-Gen IT</text>
  <line class="rule" x1="30" y1="218.5" x2="194" y2="218.5"/>
  <text class="connector" x="249" y="233" text-anchor="middle">and</text>
  <line class="rule" x1="304" y1="218.5" x2="467" y2="218.5"/>
  <text class="voip" x="30" y="368">VOIP</text>
  <text class="services" x="354" y="367">Services</text>

  <!-- tagline -->
  <text class="tagline" x="34" y="421">Seamless Technology Solutions</text>
  <text class="tagline" x="34" y="450">Tailored for <tspan class="tagline-strong">Your Business Success</tspan></text>

  <!-- call to action -->
  <text class="cta" x="739" y="385" text-anchor="middle">Transform Your Tech Today at</text>
  <text class="url" x="736" y="440" text-anchor="middle">www.<tspan class="url-strong">brivolane</tspan>.com</text>
</svg>
</body>
</html>
```